Business Card for Pimortex

I need a creative Business Card design for my start-up.
Pimortex is a Vouchers (discounts) and media publisher, logo attached.
Info to be included:
First & Last name
Mobile Number
Email
Website
Social media accounts, Facebook, Insta, Linkedin.

```html
<!DOCTYPE html>
<html lang="en">
<head>
<meta charset="utf-8">
<title>Pimortex Business Card</title>
<link href="https://fonts.googleapis.com/css2?family=Roboto:wght@400;500;700&display=swap" rel="stylesheet">
<style>
  :root {
    --backdrop: #8a8a8a;
    --navy: #241e66;
    --orange: #f29a1f;
    --orange-deep: #e0761a;
    --cream: #f6f0d6;
    --white: #ffffff;
    --ink: #241e66;
  }
  * { margin: 0; padding: 0; box-sizing: border-box; }
  html, body { width: 1200px; height: 900px; overflow: hidden; }
  body {
    background: var(--backdrop);
    font-family: "Roboto", Arial, sans-serif;
    position: relative;
  }
  .card {
    position: absolute;
    top: 295px;
    width: 520px;
    height: 310px;
    border-radius: 4px;
    overflow: hidden;
    box-shadow: 0 6px 18px rgba(0,0,0,0.25);
  }
  .card--info { left: 50px; background: var(--white); }
  .card--brand { left: 630px; background: var(--navy); }

  .card__wave { position: absolute; inset: 0; }

  .brand-mark {
    position: absolute;
    display: flex;
    align-items: center;
    font-weight: 700;
    letter-spacing: 1px;
  }
  .brand-mark__dot { border-radius: 50%; background: var(--orange-deep); flex: none; }

  .card--info .brand-mark { left: 36px; top: 34px; gap: 12px; color: var(--ink); font-size: 30px; }
  .card--info .brand-mark__dot { width: 44px; height: 44px; }

  .card--brand .brand-mark { left: 50%; top: 50%; transform: translate(-50%, -50%); gap: 20px; color: var(--cream); font-size: 60px; }
  .card--brand .brand-mark__dot { width: 80px; height: 80px; }

  .person { position: absolute; left: 36px; top: 112px; }
  .person__name { font-size: 22px; font-weight: 500; color: var(--ink); }
  .person__role { font-size: 12px; color: var(--ink); margin-top: 2px; letter-spacing: 1px; }
  .person__rule { width: 180px; height: 3px; background: var(--orange); margin-top: 8px; }

  .contacts {
    position: absolute;
    right: 24px;
    top: 108px;
    list-style: none;
    display: flex;
    flex-direction: column;
    gap: 5px;
  }
  .contact { display: flex; align-items: center; gap: 8px; }
  .contact__icon { width: 16px; height: 16px; flex: none; }
  .contact__bar {
    width: 220px;
    height: 21px;
    background: var(--orange);
    border-bottom: 3px solid var(--orange-deep);
    color: var(--navy);
    font-size: 11.5px;
    font-weight: 500;
    line-height: 18px;
    padding-left: 10px;
    border-radius: 2px;
  }
</style>
</head>
<body>
  <section class="card card--info">
    <svg class="card__wave" viewBox="0 0 520 310" aria-hidden="true">
      <path d="M0,310 L0,255 C120,250 190,195 235,135 C275,85 360,62 520,52 L520,310 Z" fill="var(--navy)"/>
    </svg>
    <div class="brand-mark"><span class="brand-mark__dot"></span>PIMORTEX</div>
    <div class="person">
      <p class="person__name">Daniel Reyes</p>
      <p class="person__role">CEO</p>
      <div class="person__rule"></div>
    </div>
    <ul class="contacts">
      <li class="contact">
        <svg class="contact__icon" viewBox="0 0 16 16"><path d="M3 1h3l1 4-2 1c1 2 3 4 5 5l1-2 4 1v3c0 1-1 2-2 2C7 15 1 9 1 3c0-1 1-2 2-2z" fill="var(--orange)"/></svg>
        <span class="contact__bar">000-000-0000</span>
      </li>
      <li class="contact">
        <svg class="contact__icon" viewBox="0 0 16 16"><rect x="1" y="3" width="14" height="10" rx="1" fill="var(--orange)"/><path d="M1 4l7 5 7-5" stroke="var(--navy)" stroke-width="1.3" fill="none"/></svg>
        <span class="contact__bar">info@yourdomain.com</span>
      </li>
      <li class="contact">
        <svg class="contact__icon" viewBox="0 0 16 16"><circle cx="8" cy="8" r="6.5" stroke="var(--orange)" stroke-width="1.5" fill="none"/><ellipse cx="8" cy="8" rx="2.8" ry="6.5" stroke="var(--orange)" stroke-width="1.2" fill="none"/><path d="M1.5 8h13" stroke="var(--orange)" stroke-width="1.2"/></svg>
        <span class="contact__bar">www.yourdomain.com</span>
      </li>
      <li class="contact">
        <svg class="contact__icon" viewBox="0 0 16 16"><rect x="2" y="2" width="12" height="12" rx="2" fill="var(--orange)"/></svg>
        <span class="contact__bar">pimortex.official</span>
      </li>
      <li class="contact">
        <svg class="contact__icon" viewBox="0 0 16 16"><rect x="2" y="2" width="12" height="12" rx="2" fill="var(--orange)"/></svg>
        <span class="contact__bar">Pimortex</span>
      </li>
      <li class="contact">
        <svg class="contact__icon" viewBox="0 0 16 16"><circle cx="8" cy="8" r="6" fill="var(--orange)"/></svg>
        <span class="contact__bar">pimortex_media</span>
      </li>
      <li class="contact">
        <svg class="contact__icon" viewBox="0 0 16 16"><path d="M8 15s5-5 5-9A5 5 0 0 0 3 6c0 4 5 9 5 9z" fill="var(--orange)"/><circle cx="8" cy="6" r="1.8" fill="var(--navy)"/></svg>
        <span class="contact__bar">2581 Cedar Lane, Brookfield, Canada</span>
      </li>
    </ul>
  </section>

  <section class="card card--brand">
    <div class="brand-mark"><span class="brand-mark__dot"></span>PIMORTEX</div>
  </section>
</body>
</html>
```